Anzeigengestaltung für Gebäudedienstleistungsunternehmen
Zielgruppe
Wir sind ein lokales Gebäudedienstleistungsunternehmen und bieten Gebäudereinigung und Haushaltsreinigung, Grünanlagenpflege und Gartenpflege, Winterdienst und Hausmeisterservice für Privat- und Gewerbekunden an.
Aufgabenstellung
Zur Info: Wir benötigen auch ein Flyerdesign. Dieses möchten wir in Anschluss an diesen Auftrag als 1-zu-1 Projekt an den Designer unserer Anzeige vergeben.
Diese Anzeige soll in dem lokalen Mitteilungsblatt (https://www.ortsbote-velun.com/index.php) erscheinen.
Es ist eine farbige zweispaltige (92mm) Anzeige mit der Höhe von 50mm.
Unser Logo und die Firmenfarben sollen verwendet werden. Gerne darf auch ein Foto benutzt werden (z.B. im Hintergrund), welches nach den Jahreszeiten gewechselt werden kann. Zum Beispiel: Frühjahr -> Gartenpflege, Sommer -> Gebäudereinigung, Herbst -> Winterdienst und im Winter -> Hausmeisterservice.
Der Text sollte unsere Dienstleistungen enthalten. Diese sind: Gebäude- und Haushaltsreinigung, Grünanlagen- und Gartenpflege, Winterdienst und Hausmeisterservice. Zusätzlich der Hinweis, dass wir sowohl Privat als auch Gewerbekunden ansprechen möchten.
Unsere Kontaktdaten sollen auch enthalten sein:
Internet: www.brimato.de, Telefon: 09471/3582140, E-Mail: kontakt@brimato.de
Falls es noch Platz gibt, dann wäre es schön noch den lokalen Bezug herzustellen, indem man die Postleitzahl und den Ort unserer Firma nennt. Eine Nennung der Straße ist nicht vorgesehen.
PLZ: 91207 Ort: Lauf an der Pegnitz od. Lauf a.d. Pegnitz

```html
<!DOCTYPE html>
<html lang="de">
<head>
<meta charset="utf-8">
<title>Brimato Gebäudedienste – Anzeige</title>
<link rel="stylesheet" href="https://fonts.googleapis.com/css2?family=Poppins:wght@800&family=Roboto:wght@300;400;500;700&display=swap">
<style>
  :root {
    --brand-blue: #0072ab;
    --panel-blue: rgba(14, 92, 140, 0.93);
    --badge-blue: #1d7db9;
    --white: #ffffff;
    --page-top: #ffffff;
    --page-bottom: #f1f1f1;
    --photo-dark: #1f3a2a;
    --photo-mid: #4d6a45;
    --photo-light: #c9cfd2;
  }
  * { margin: 0; padding: 0; box-sizing: border-box; }
  html, body { width: 1166px; height: 1200px; overflow: hidden; }
  body {
    background: linear-gradient(to bottom, var(--page-top) 0 611px, var(--page-bottom) 611px 100%);
    font-family: "Roboto", Arial, sans-serif;
    color: var(--white);
    position: relative;
  }
  .ad {
    position: absolute;
    left: 59px; top: 83px;
    width: 1064px; height: 578px;
    overflow: hidden;
  }
  .ad-photo {
    position: absolute; left: 0; top: 0; width: 1064px; height: 500px;
    background:
      linear-gradient(100deg, var(--photo-dark) 0%, var(--photo-mid) 45%, #6b7468 62%, var(--photo-light) 85%, #e3e4e2 100%);
  }
  .ad-panel {
    position: absolute; left: 0; top: 0; width: 606px; height: 473px;
    background: linear-gradient(160deg, rgba(20,100,150,0.9), var(--panel-blue));
    clip-path: polygon(0 0, 606px 0, 459px 473px, 0 473px);
  }
  .headline {
    position: absolute; left: 21px; top: 20px;
    font-family: "Poppins", Arial, sans-serif; font-weight: 800;
    font-size: 61px; line-height: 65px; letter-spacing: -0.5px;
    text-shadow: 0 3px 8px rgba(0,0,0,0.35);
  }
  .services {
    position: absolute; left: 21px; top: 160px;
    font-weight: 300; font-size: 28px; line-height: 34.5px;
  }
  .call-label {
    position: absolute; left: 21px; top: 344px;
    font-size: 27px; font-weight: 400; line-height: 30px;
  }
  .phone {
    position: absolute; left: 20px; top: 368px;
    font-size: 49px; font-weight: 700; line-height: 50px; letter-spacing: 0.5px;
  }
  .email {
    position: absolute; left: 23px; top: 424px;
    font-size: 31px; font-weight: 700; line-height: 36px;
  }
  .audience-badge {
    position: absolute; left: 800px; top: 0; width: 250px; height: 156px;
    background: var(--badge-blue);
    clip-path: polygon(49px 0, 250px 0, 217px 156px, 0 156px);
  }
  .audience-badge p {
    position: absolute; left: 30px; width: 200px; top: 22px;
    text-align: center; font-weight: 500; font-size: 38px; line-height: 33px;
  }
  .ad-footer {
    position: absolute; left: 0; top: 500px; width: 1064px; height: 78px;
    background: var(--brand-blue);
  }
  .web {
    position: absolute; left: 30px; top: 17px;
    font-size: 36px; font-weight: 400; line-height: 42px;
  }
  .company {
    position: absolute; right: 18px; top: 12px;
    display: flex; align-items: center; gap: 14px;
  }
  .company-mark { width: 30px; height: 30px; background: var(--white); }
  .company-name {
    font-family: "Poppins", Arial, sans-serif; font-weight: 800;
    font-size: 25px; line-height: 26px; text-transform: uppercase;
  }
</style>
</head>
<body>
  <section class="ad">
    <div class="ad-photo" role="img" aria-label="Foto: Gärtner mit Schutzhelm mäht mit einem Freischneider den Rasen vor einem hellen Haus mit Palme im Kübel"></div>
    <div class="ad-panel"></div>
    <h1 class="headline">Alles im grünen<br>Bereich</h1>
    <p class="services">Nutzen Sie unseren Rundum-service:<br>Gebäude- und Haushaltsreinigung,<br>Grünanlagen- und Gartenpflege,<br>Winterdienst und Hausmeisterservice.</p>
    <p class="call-label">RUFEN SIE UNS GERNE AN!</p>
    <p class="phone">09471 358 2140</p>
    <p class="email">kontakt@brimato.de</p>
    <div class="audience-badge"><p>Privat-<br>&amp;<br>Gewerbe!</p></div>
    <footer class="ad-footer">
      <p class="web">www.brimato.de</p>
      <div class="company">
        <span class="company-mark"></span>
        <span class="company-name">Brimato<br>Gebäudedienste</span>
      </div>
    </footer>
  </section>
</body>
</html>
```